Redesign Of Hotel Coupon/Voucher 8.5 x 11

I would like to redesign my voucher.

Please provide me a color flyer design but one that would be easy on printing costs...for example printing from home computer/printer.

I would like to see some color designs...maybe some black and white and also full graphics and even basic like the plum rook voucher I provided as a sample. The 2 night hotel stay is the voucher I need to redesign...

Target Market(s)

Consumers

Industry/Entity Type

Hotel

Requirements
Must have
• exact text in current designs---look official, credible and trust worthy
Nice to have
• I would like to redesign my voucher.
• Please provide me a color flyer design but one that would be easy on printing costs...for example printing from home computer/printer.
• I would like to see some color designs...maybe some black and white and also full graphics and even basic like the plum rook voucher I provided as a sample. The 2 night hotel stay is the voucher I need to redesign...
Should not have

```html
<!DOCTYPE html>
<html lang="en">
<head>
<meta charset="utf-8">
<title>2 Night Hotel Stay Certificate</title>
<link href="https://fonts.googleapis.com/css2?family=Bowlby+One+SC&family=Source+Sans+3:wght@400;600;700&display=swap" rel="stylesheet">
<style>
:root{
  --navy:#2b3144;
  --red:#e8505b;
  --red-dark:#c93a46;
  --green:#8dc63f;
  --ink:#2a2a2a;
  --muted:#5a5a5a;
  --rule:#9a9a9a;
  --page-bg:#e9e9ea;
  --white:#ffffff;
}
*{box-sizing:border-box;margin:0;padding:0}
html,body{width:1147px;height:1200px;overflow:hidden;background:var(--page-bg)}
body{font-family:"Source Sans 3",Arial,sans-serif;color:var(--ink);position:relative}
.voucher{position:absolute;left:148px;top:50px;width:850px;height:1100px;background:var(--navy);border-radius:10px;padding:18px}
.sheet{position:relative;width:100%;height:100%;background:var(--white);border-radius:14px;overflow:hidden}
.hero-photo{position:absolute;left:0;top:0;width:450px;height:235px;background:linear-gradient(135deg,#3f8c8c 0%,#b7b98c 45%,#e8e2c4 75%,#f3efe2 100%)}
.hero-fade{position:absolute;left:300px;top:0;width:514px;height:235px;background:linear-gradient(90deg,rgba(255,255,255,0),#fff 40%)}
.compliments{position:absolute;right:40px;top:28px;width:260px}
.compliments h2{font-weight:600;font-size:17px;line-height:19px;color:#555;letter-spacing:.5px;border-bottom:2px solid #555;padding-bottom:6px;margin-bottom:10px}
.field-line{display:flex;align-items:flex-end;font-size:10px;color:#666;height:21px;margin-left:12px}
.field-line span{flex:1;border-bottom:1px dotted #888;margin-left:3px;height:10px}
.title-rule{position:absolute;left:0;right:0;top:208px;height:3px;background:var(--red)}
.title-banner{position:absolute;left:120px;top:165px;width:420px;height:72px;background:var(--red);border:3px solid var(--red-dark);outline:2px solid var(--white);outline-offset:-8px;display:flex;align-items:center;justify-content:center;transform:skewX(-6deg)}
.title-banner h1{font-family:"Bowlby One SC","Arial Black",sans-serif;font-weight:400;color:var(--white);font-size:31px;letter-spacing:1.5px;transform:skewX(6deg)}
.destinations{position:absolute;left:30px;right:30px;top:262px;font-size:10.6px;line-height:13.5px;text-align:center;color:#333}
.terms-head{position:absolute;left:50px;right:50px;top:346px;display:flex;align-items:center;gap:10px;color:var(--red);font-size:12px;letter-spacing:.3px}
.terms-head::before,.terms-head::after{content:"";flex:1;height:1px;background:var(--red)}
.terms{position:absolute;left:24px;right:24px;top:368px;font-size:9.3px;line-height:12.3px;text-align:justify;color:#333}
.bell-divider{position:absolute;left:24px;right:24px;top:580px;height:20px}
.bell-divider::before{content:"";position:absolute;left:0;right:0;top:15px;height:1px;background:#444}
.bell-divider svg{position:absolute;left:50%;top:0;margin-left:-11px;background:var(--white)}
.redeem-panel{position:absolute;left:0;top:610px;width:218px;height:300px;background:var(--green);color:var(--white);padding:14px 12px;font-size:10.5px;line-height:13px}
.redeem-panel .pay-note{border-bottom:1px dotted var(--white);padding-bottom:10px;margin-bottom:10px}
.redeem-panel ol{list-style:none;font-weight:700}
.redeem-panel .link{color:#1f5fa8}
.cert-id{position:absolute;left:14px;top:924px;font-weight:700;font-size:14px;line-height:18px}
.cert-id .exp{color:var(--red)}
.form-col{position:absolute;font-size:9.5px;color:#444}
.form-col h3{font-size:14px;font-weight:700;color:#333;letter-spacing:.3px;margin-bottom:4px}
.form-row{display:flex;align-items:flex-end;height:13.5px}
.form-row label{width:42px}
.form-row span{flex:1;border-bottom:1px solid #777;height:8px}
.billing{left:232px;top:618px;width:230px}
.shipping{left:232px;top:840px;width:230px}
.payment{left:500px;top:612px;width:290px}
.payment h4{font-size:12px;font-weight:700;color:#333;margin-bottom:8px}
.pay-grid{display:grid;grid-template-columns:1fr 1fr;row-gap:3px;margin-bottom:20px}
.check{display:flex;align-items:center;gap:5px}
.check i{width:8px;height:8px;border:1px solid #555}
.payment .form-row label{width:70px}
.agree{margin-top:28px;font-weight:700;color:#333}
.agree .form-row{font-size:10px}
.fine-print{margin-top:8px;font-size:7.5px;line-height:9.5px}
.code-tag{position:absolute;right:0;bottom:36px;background:var(--green);color:var(--navy);font-size:9px;font-weight:700;padding:3px 10px 3px 16px;border-radius:10px 0 0 0}
</style>
</head>
<body>
<main class="voucher">
  <section class="sheet">
    <div class="hero-photo" role="img" aria-label="Photo of a hotel room breakfast tray on a bed by a sunlit window"></div>
    <div class="hero-fade"></div>

    <div class="compliments">
      <h2>THE CERTIFICATE IS<br>COMPLIMENTS OF:</h2>
      <div class="field-line">NAME<span></span></div>
      <div class="field-line">PH<span></span></div>
      <div class="field-line">E-MAIL<span></span></div>
    </div>

    <div class="title-rule"></div>
    <div class="title-banner"><h1>2 NIGHT HOTEL STAY</h1></div>

    <p class="destinations">Destinations Available: Anaheim, CA--Atlanta, GA--Atlantic City, NJ--Branson, MO--Cancun, MX--Charleston, SC--Coeur d' Alene, ID--Daytona Beach, FL--Destin, FL--Ft. Lauderdale, FL--Ft. Meyers, FL--Gatlinburg, TN--Hilton Head, SC--Honolulu, HI--Kissimmee, FL--Lake Tahoe, CA--Las Vegas, NV--Myrtle Beach, SC--Niagara Falls/Buffalo Area, NY--Orlando, FL--Ormond Beach, FL--Palm Springs, CA--Pigeon Forge, TN--St. Petersburg, FL--San Antonio, TX--San Diego, CA--San Francisco, CA--Sedona, AZ--Sonoma Wine Country, CA--St. George, UT--Tampa, FL--Williamsburg, VA--Wisconsin Dells, WI--Tallahassee, FL--Augusta, GA--Columbia, SC--New York, NY--Florence, SC--Washington, D.C.--Chicago, IL--Salt Lake City, UT--Hollywood, CA--Dayton, OH--Tucson, AZ--Niagra Falls, ON/CAN--Seattle, WA--Portland, OR--Antioch, CA--San Mateo, CA--Brunswick, GA--Nashville, TN</p>

    <div class="terms-head">TERMS &amp; CONDITIONS</div>
    <p class="terms">This certificate will be considered void if bartered or purchased for legal tender by the recipient. This certificate is valid for a reservation request form offering 2 adults 21 years of age and older plus up to 2 children under the age of 18, 2 nights of hotel accommodations in the city of their choice of available cities. The cost to activate this certificate to receive the reservation request form is just a one-time non-refundable $14.95 processing fee. The cost upon requesting reservations is just a tax &amp; fee deposit of $33 per night. Taxes &amp; fees usually range from $12-$33 per night depending on when and where you travel to. If the taxes &amp; fees are less than the $33 per night the difference will be refunded after travel is completed. 30 days advance reservation notice is required. In order to guarantee that you will show up to your booked reservation you will be required to pay a REFUNDABLE $50 "Reservation Guarantee Deposit". If you send in your travel dates, etc and you do not end up traveling then the reservation guarantee deposit will not be refundable. 7 days before and after holidays and conventions are not available. This offer is valid 7 days a week subject to availability. Friday and Saturday nights will require a surcharge of $20 per night. A $5 per person per night surcharge is enforced for each child up to 2 children under the age of 18. This offer is not valid for group travel. The recipient of this certificate is responsible for all expenses including but not limited to: transfers, food, gratuities, all pertinent fees, taxes, hotel surcharges, resort fees and any other miscellaneous expenses. If you activate this certificate online you will be able to instantly print your reservation request form. If you cannot print your own reservation request form we will mail it to you. You should receive it in the mail within 14 days. This certificate cannot be combined with any other promotional vacation offer. The expiration date on this certificate pertains only to activation of this certificate and not actual travel. You must activate this certificate by the expiration date printed on this certificate in order to receive the reservation request form. You must fill out the reservation request form with your destination choices and arrival dates and mail it to our fulfillment department within 6 months after activation, however travel can be completed within 12 months after activation. You will be required to give the travel agency multiple arrival dates and destinations. Only one 2 Night Hotel certificate Per Household Per Year. This certificate has no cash surrender value, void if discontinued and where prohibited by law. The terms of this offer are subject to change without notice. Do not rely upon representations other than what is printed on this certificate or the reservation request form. CST # 4417380</p>

    <div class="bell-divider">
      <svg width="22" height="18" viewBox="0 0 22 18" aria-hidden="true"><path d="M3 14a8 8 0 0 1 16 0z" fill="none" stroke="#444" stroke-width="1.6"/><circle cx="11" cy="4.5" r="1.5" fill="#444"/><line x1="1" y1="15.5" x2="21" y2="15.5" stroke="#444" stroke-width="1.6"/></svg>
    </div>

    <aside class="redeem-panel">
      <p class="pay-note">Simply fill out the form on this certificate and enclose payment of U.S. $14.95. Veyra, Meridian Card, Axion Express, Dovetail, Debit Card, Check Card, Check &amp; Money Orders are all accepted.</p>
      <ol>
        <li>3 Ways To Redeem:</li>
        <li>1. For expedited redemption go to:<br><span class="link">www.StayPerksClub.com</span></li>
        <li>2. Fax* certificate to: 1-888-555-0142</li>
        <li>3. Mail* to:<br>Redemption Center<br>4210 Harbor View Rd Ste B #118<br>Bay Ridge, Ca 90000</li>
      </ol>
    </aside>
    <p class="cert-id">Certificate ID: -10002<br>Expiration Date: <span class="exp">04/08/2017</span></p>

    <section class="form-col billing">
      <h3>BILLING INFORMATION</h3>
      <div class="form-row"><label>Name:</label><span></span></div>
      <div class="form-row"><label>Address:</label><span></span></div>
      <div class="form-row"><label></label><span></span></div>
      <div class="form-row"><label>City:</label><span></span></div>
      <div class="form-row"><label>State:</label><span></span></div>
      <div class="form-row"><label>Zip Code:</label><span></span></div>
      <div class="form-row"><label>Country:</label><span></span></div>
      <div class="form-row"><label>Phone:</label><span></span></div>
      <div class="form-row"><label>Email:</label><span></span></div>
    </section>

    <section class="form-col shipping">
      <h3>SHIPPING INFORMATION</h3>
      <div class="form-row"><label>Name:</label><span></span></div>
      <div class="form-row"><label>Address:</label><span></span></div>
      <div class="form-row"><label></label><span></span></div>
      <div class="form-row"><label>City:</label><span></span></div>
      <div class="form-row"><label>State:</label><span></span></div>
      <div class="form-row"><label>Zip Code:</label><span></span></div>
      <div class="form-row"><label>Country:</label><span></span></div>
    </section>

    <section class="form-col payment">
      <h3>PAYMENT INFORMATION</h3>
      <h4>Payment Method:</h4>
      <div class="pay-grid">
        <div class="check"><i></i>Check</div>
        <div class="check"><i></i>Money Order</div>
        <div class="check"><i></i>Veyra</div>
        <div class="check"><i></i>Meridian Card</div>
        <div class="check"><i></i>Axion</div>
        <div class="check"><i></i>Dovetail Card</div>
      </div>
      <div class="form-row"><label>Name On Card:</label><span></span></div>
      <div class="form-row"><label>Card # (16 digits):</label><span></span></div>
      <div class="form-row"><label>Expiration Date:</label><span></span></div>
      <div class="form-row"><label>CV2#**</label><span></span></div>
      <div class="agree">
        <p>I agree to terms and conditions</p>
        <div class="form-row"><label>Signature:</label><span></span></div>
      </div>
      <p class="fine-print">*"Redemption Center" will appear on your billing statement.<br>Make checks and money orders payable to: "Redemption Center"<br>* You will receive your information by mail within 10 days.<br>** Last 3 digits on back of card (4 digits on front of Axion).</p>
    </section>

    <div class="code-tag">2NIL-10002</div>
  </section>
</main>
</body>
</html>
```